Wellness Web Design Project

web design for business called Lumen Harbor Wellness. I have a private practice for which i need patients. I teach in house and online courses for professional and the public. It will be both an educational site as well as a marketing site and it will have a store and a member login area. I do sonic acupuncture called vibrelaxis. It is based on demarchetos' music of the spheres. I use vibrational and harmonic therapies to harmonize cells psyches and souls! it is the most scientifically rooted of the alternative therapies available and i focus on womens health, pediatric, emotional problems and spiritual awakening. I need it to be a balance of spiritual and symbolic depth as well as being graceful sophisticated grounded. I want it to look incredibly elegant, sophisticated, and established, not airy fairy! i like a minimal approach, fresh air, clean, confident, expensive, luxurious but also playful. im not trying to mold myself into the usual framework. i am trying to convey a sense of unleashing power and purpose and pleasure. i need it to be Gorgeous and relatable while being original
i have included the site map as an upload and here is a link to all the things that a home page should include. I have the logo and other versions that i will use to promote the different online programs i have. I may have a 'sound logo' start as the page comes up. the sounds are ethereal tones rather than music and super gentle and mysterious without being cloying or overly emotional. I work with the physical body, emotional trauma and altered states so many hats and have many different prongs to what i do so organization and clarity is important without getting cluttered. want to convert and capture into my email list for sure and have free downloadable content to provide.
the logo i have designed speaks volumes about my aesthetic. i have included a flyer made - which is 1. direction, but i am interested in seeing some designs that play with white space as well. the 'look' of the flyer has never been published and so am in no way married to it. I will include some of the photo i will want to use along the way that give you some sense of things or things to riff off. some of the photos of me have alot of solid blocks of color... i have included one of them. I am very sensitive to sophistication of color.
the site map i have included is jsut my attempt to organize - i am not married to it!
thankyou so much, and if you haven;t yet discovered the power of sound to alter brain waves and cell functioning wherever you are in the world - I highly recommend it:)

Target Market(s)

women 25-55's educated, familiar with alternative healing and conscious living who have money to spend on wellness

Industry/Entity Type

Business

Requirements
Must have
• http://notes.brimfaldo.com/notes/tabid/4821/bid/58204/12-Critical-Elements-Every-Homepage-Must-Have-Infographic.aspx
these are some of the elements that seem to be necessary
plus social media links....

```html
<!DOCTYPE html>
<html lang="en">
<head>
<meta charset="utf-8">
<title>Lumen Harbor Wellness</title>
<link rel="stylesheet" href="https://fonts.googleapis.com/css2?family=Roboto+Condensed:wght@400;700&family=Arimo:ital,wght@0,400;0,700;1,400&display=swap">
<style>
:root{
  --ink:#333333;
  --text:#555555;
  --muted:#6a6a6a;
  --orange:#f7941d;
  --orange-light:#f5b335;
  --green:#1e8a1e;
  --rule:#cfcfcf;
  --footer:#333333;
  --white:#ffffff;
}
*{box-sizing:border-box;margin:0;padding:0}
html,body{width:1200px;height:1134px;overflow:hidden;background:var(--white)}
body{position:relative;font-family:"Arimo",Arial,sans-serif;color:var(--text)}
.top-bar{position:absolute;left:0;top:0;width:1200px;height:10px;background:var(--footer)}

.brand{position:absolute;left:122px;top:44px;display:flex;align-items:center;gap:14px}
.brand-dot{width:60px;height:60px;border-radius:50%;background:var(--orange)}
.brand-name{font-family:"Roboto Condensed",sans-serif;font-weight:400;font-size:31px;color:var(--orange);letter-spacing:.5px;text-transform:uppercase}

.main-nav{position:absolute;right:121px;top:66px;display:flex;gap:38px}
.main-nav a{font-family:"Roboto Condensed",sans-serif;font-size:18px;color:var(--muted);text-decoration:none;letter-spacing:.5px}

.hero{position:absolute;left:120px;top:141px;width:960px;height:380px;background:linear-gradient(100deg,#f5a623 0%,#f7941d 35%,#f3ad33 100%)}
.hero-title{position:absolute;left:20px;top:32px;font-family:"Roboto Condensed",sans-serif;font-size:47px;font-weight:400;color:var(--white);letter-spacing:.5px}
.hero-title span{color:var(--ink)}
.hero-copy{position:absolute;left:20px;top:95px;width:404px;font-size:12.6px;line-height:18px;color:var(--white);text-align:justify}
.hero-list{position:absolute;left:20px;top:180px;list-style:none}
.hero-list li{display:flex;align-items:center;gap:12px;height:30px;font-size:13px;font-style:italic;color:var(--white)}
.hero-list svg{width:14px;height:14px}
.btn-book{position:absolute;left:12px;top:303px;width:207px;height:39px;border:1px solid #c8c8c8;border-radius:3px;background:linear-gradient(#ffffff,#e2e2e2);font-family:"Roboto Condensed",sans-serif;font-size:17px;color:#8a8a8a;display:flex;align-items:center;justify-content:center;letter-spacing:.3px}
.slider-dots{position:absolute;left:10px;top:355px;display:flex;gap:11px}
.slider-dots i{width:10px;height:10px;border-radius:50%;background:#e49720;display:block}
.slider-dots i.active{background:#5a4a2a}
.video-frame{position:absolute;left:474px;top:41px;width:470px;height:300px;background:var(--white);box-shadow:0 1px 4px rgba(0,0,0,.25);padding:8px}
.video-still{width:454px;height:284px;background:linear-gradient(135deg,#2a6f86 0%,#c99a7e 45%,#5a3a2a 70%,#b8303a 100%);position:relative}
.play{position:absolute;left:197px;top:124px;width:62px;height:42px;border-radius:8px;background:rgba(30,30,30,.75);display:flex;align-items:center;justify-content:center}

.column{position:absolute;top:552px;width:300px}
.column h2{font-family:"Roboto Condensed",sans-serif;font-weight:400;font-size:24px;color:var(--muted);padding-left:1px;height:39px}
.column .bar{height:5px;background:var(--orange);margin-bottom:12px}
.col-a{left:120px}.col-b{left:450px}.col-c{left:779px}
.testimonial-lead{display:flex;gap:9px}
.portrait{flex:none;width:120px;height:105px;background:linear-gradient(135deg,#7a4a30,#c98a6a,#5b3a26)}
.quote{font-size:12px;line-height:17px;text-align:justify;color:var(--text)}
.quote-rest{margin-top:6px;padding-bottom:6px;border-bottom:1px solid var(--rule)}
.service{padding:10px 0 7px;border-bottom:1px solid var(--rule)}
.service:first-of-type{padding-top:0}
.service h3{font-size:13px;font-weight:400;color:var(--green);margin-bottom:3px}
.service p{font-size:12px;line-height:19px;color:var(--text)}
.review{display:flex;gap:6px;padding-bottom:7px;border-bottom:1px solid var(--rule);margin-bottom:8px}
.review .avatar{flex:none;width:80px;height:64px;background:linear-gradient(135deg,#f2f2f2,#c9a58a,#3b2a22)}
.review-body .quote{font-style:italic;line-height:18px}
.review-name{font-size:12px;font-style:italic;color:var(--text);margin-top:4px;margin-left:-86px}
.review-name b{font-style:normal;font-weight:400;color:var(--orange)}
.btn-more{position:absolute;top:272px;left:-1px;width:89px;height:32px;background:linear-gradient(#f7a623,#f7941d);color:var(--white);font-family:"Roboto Condensed",sans-serif;font-size:14px;display:flex;align-items:center;justify-content:center}

.partners{position:absolute;left:0;top:890px;width:1200px;height:163px;background:radial-gradient(ellipse 600px 14px at 600px 0,rgba(0,0,0,.08),transparent)}
.partner{position:absolute}

.site-footer{position:absolute;left:0;top:1053px;width:1200px;height:81px;background:var(--footer)}
.footer-links{position:absolute;left:130px;top:19px;font-size:12px;color:#e6e6e6}
.footer-links span{margin:0 6px}
.copyright{position:absolute;left:130px;top:49px;font-size:12px;color:#e6e6e6}
.social{position:absolute;left:858px;top:21px;display:flex;gap:8px}
.social i{width:32px;height:32px;display:block}
</style>
</head>
<body>
<div class="top-bar"></div>

<header>
  <div class="brand"><span class="brand-dot"></span><span class="brand-name">Lumen Harbor Wellness</span></div>
  <nav class="main-nav">
    <a href="#">ABOUT</a><a href="#">SERVICES</a><a href="#">THERABIES</a><a href="#">GALLERY</a><a href="#">CONTACT</a>
  </nav>
</header>

<section class="hero">
  <h1 class="hero-title"><span>SONIC</span> ACUPUNTURE</h1>
  <p class="hero-copy">Perspiciatis unde omnis iste natus error sit voluptatem accusantium doloremque laudantium, totam rem aperiam, eaque ipsa quae ab illo inventore veritatis et quasi architecto beatae vitae dicta sunt explicabo.aut odit aut fugit.</p>
  <ul class="hero-list">
    <li><svg viewBox="0 0 14 14"><rect x=".5" y="2.5" width="11" height="11" fill="none" stroke="#333"/><path d="M3 7l3 3 7-9" fill="none" stroke="#333" stroke-width="2"/></svg>perspiciatis unde omnis iste natus sit</li>
    <li><svg viewBox="0 0 14 14"><rect x=".5" y="2.5" width="11" height="11" fill="none" stroke="#333"/><path d="M3 7l3 3 7-9" fill="none" stroke="#333" stroke-width="2"/></svg>Voluptatem accusantium doloremque</li>
    <li><svg viewBox="0 0 14 14"><rect x=".5" y="2.5" width="11" height="11" fill="none" stroke="#333"/><path d="M3 7l3 3 7-9" fill="none" stroke="#333" stroke-width="2"/></svg>laudantium totam rem aperiam eaque</li>
    <li><svg viewBox="0 0 14 14"><rect x=".5" y="2.5" width="11" height="11" fill="none" stroke="#333"/><path d="M3 7l3 3 7-9" fill="none" stroke="#333" stroke-width="2"/></svg>ipsa quae inventore veritatis et quasi</li>
  </ul>
  <div class="btn-book">BOOK AN APPOINTMENT</div>
  <div class="slider-dots"><i class="active"></i><i></i><i></i></div>
  <div class="video-frame">
    <div class="video-still" role="img" aria-label="Video still: tuning forks placed on a client's head during a sound treatment">
      <div class="play"><svg width="20" height="22" viewBox="0 0 20 22"><path d="M2 1l17 10L2 21z" fill="#e8e8e8"/></svg></div>
    </div>
  </div>
</section>

<section class="column col-a">
  <h2>Our Cusotmer Says</h2>
  <div class="bar"></div>
  <div class="testimonial-lead">
    <div class="portrait" role="img" aria-label="Portrait photo of a smiling client"></div>
    <p class="quote">“Totam rem aperiam, eaque ipsa quae ab illo inventore veri-tatis et quasi architecto beata perspiciatis unde omnis iste ccusantium doloremque laudanti ”architecto beata</p>
  </div>
  <p class="quote quote-rest">“Totam rem aperiam, eaque ipsa quae ab illo inventore veritatis et quasi architecto beata perspiciatis unde omnis iste ccusantium doloremque laudanti ”architecto beata perspiciatis unde omnis iste ccusantium doloremque laudanti ”</p>
  <a class="btn-more">READ MORE</a>
</section>

<section class="column col-b">
  <h2>Our Services</h2>
  <div class="bar"></div>
  <div class="service"><h3>perspiciatis unde omnis iste natus error</h3><p>totam rem aperiam, eaque ipsa quae ab illo inventore veritatis et quasi architecto beatae</p></div>
  <div class="service"><h3>perspiciatis unde omnis iste natus error</h3><p>totam rem aperiam, eaque ipsa quae ab illo inventore veritatis et quasi architecto beatae</p></div>
  <div class="service"><h3>perspiciatis unde omnis iste natus error</h3><p>totam rem aperiam, eaque ipsa quae ab illo inventore veritatis et quasi architecto beatae</p></div>
  <a class="btn-more">READ MORE</a>
</section>

<section class="column col-c">
  <h2>Our Cusotmer Says</h2>
  <div class="bar"></div>
  <div class="review">
    <div class="avatar" role="img" aria-label="Client portrait photo"></div>
    <div class="review-body"><p class="quote">“Totam rem aperiam, eaque ipsa quae ab illo inventore veritatis et quasi archi-tecto beata perspiciatis unde omnis iste ccusantium doloremque laudanti ”</p>
    <p class="review-name"><b>KATE,</b> Lorem lipsum</p></div>
  </div>
  <div class="review">
    <div class="avatar" role="img" aria-label="Client portrait photo"></div>
    <div class="review-body"><p class="quote">“Totam rem aperiam, eaque ipsa quae ab illo inventore veritatis et quasi archi-tecto beata perspiciatis unde omnis iste ccusantium doloremque laudanti ”</p>
    <p class="review-name"><b>KATE,</b> Lorem lipsum</p></div>
  </div>
  <a class="btn-more">READ MORE</a>
</section>

<section class="partners" aria-label="Partners and accreditations">
  <div class="partner" role="img" aria-label="Award seal" style="left:172px;top:37px;width:76px;height:76px;border-radius:50%;background:#ecc85a"></div>
  <div class="partner" role="img" aria-label="Partner badge" style="left:308px;top:48px;width:116px;height:72px;background:#e9e9e9"></div>
  <div class="partner" role="img" aria-label="Certification badge" style="left:476px;top:38px;width:180px;height:92px;background:#dde6f3"></div>
  <div class="partner" role="img" aria-label="Awards badge" style="left:708px;top:52px;width:156px;height:72px;background:#efefef"></div>
  <div class="partner" role="img" aria-label="Community partner badge" style="left:908px;top:46px;width:124px;height:76px;background:#eef1f6"></div>
</section>

<footer class="site-footer">
  <p class="footer-links">Privacy Policy<span>|</span>Terms of Use<span>|</span>Sitemap</p>
  <p class="copyright">Copyright ©&nbsp; 2013 Lumen Harbor Studio. All Rights Reserved.</p>
  <div class="social" aria-label="Social media links">
    <i style="background:#3b5998"></i><i style="background:#1ea1e0"></i><i style="background:#d9452f"></i><i style="background:#c4161c"></i><i style="background:#d8232a"></i><i style="background:#f37021"></i>
  </div>
</footer>
</body>
</html>
```